Plumbing Contractor Website Design

We are working with a Plumbing contractor in CA called KT Plumbline.

Some sites to use for content/competitors and inspiration:

https://www.pipevalex.com
https://www.drainmoss.com
https://quillbark.example/web/contractor/ (lots of contractor website designs we've approved and continue to show clients)

Thank you for taking the time to consider designing a website for us. We are web developers based in Stockton, CA, USA. Most of our projects go through the same process. Understanding this process may help you win a project with us. We custom-code all of our websites in-house. We don’t have any requirements as to what tools you use for your design, but we prefer Figma files. For any design that we label as four-stars, we send it to the client for review. The client picks the final design they want us to use. Once we complete this process, we will continue to show additional clients all the four-star sites and purchase them later. Your designs will have multiple chances to sell. For better chances of success, we ask that you follow these guidelines.

IMAGES:
If you use any images or icons in the design, we ask that you have a link to the asset so we can purchase the image/icon. Most of the designs we submit do not have the customer’s images on them unless they have some great images. Be creative; show us the feeling you are trying to portray with your image choices. Use any royalty-free site you choose. We subscribe to Adobe and mainly use their images, but we can purchase images outside of Adobe.

PLEASE NOTE: we will not submit designs to clients with watermarks on the images.

FONTS:
We ask that you identify the fonts used in the design. This can be done in a message if you want. We typically use Google Fonts and Adobe Fonts.

CONTENT:
We're always open to different content and ideas. We often submit designs with stock images so the client can see our vision. We typically take pictures after the website launch to use their images with our vision. Lorem Ipsum is fine for paragraphs, but we ask that you write the headers in correct English. We want to be able to show the vision and identify the sections of the website.

INSPIRATION:
We typically add a couple of links in the brief of websites we like to help you get started in your design.

REVISIONS:
We do not often ask for revisions of the designs unless we see something in the design that may not appeal to the client. If there are slight changes that we want to make, we do that in the development process.

FEEDBACK:
We rarely give feedback on designs during the design process. We are working on many website projects and do not have the time to provide feedback. We usually respond if your request is well thought out and asks specific questions, but a note asking “feedback, please” usually goes unanswered

```html
<!DOCTYPE html>
<html lang="en">
<head>
<meta charset="utf-8">
<title>KT Plumbline — Expert Plumbing Services</title>
<link rel="stylesheet" href="https://fonts.googleapis.com/css2?family=Poppins:wght@400;500;600;700&display=swap">
<style>
:root{
  --blue:#0b6e99;
  --blue-dark:#095a7e;
  --accent:#1d8fc2;
  --ink:#1b1b1b;
  --text:#2e2e2e;
  --muted:#555;
  --white:#fff;
  --services-bg-a:#b7d8e6;
  --services-bg-b:#e4eef3;
  --footer:#3d3d3d;
  --footer-line:#6a6a6a;
}
*{box-sizing:border-box;margin:0;padding:0}
html,body{width:1200px;height:4184px;overflow:hidden}
body{position:relative;font-family:"Poppins",sans-serif;color:var(--text);background:var(--white)}
.abs{position:absolute}
.btn{position:absolute;display:flex;align-items:center;justify-content:center;gap:12px;background:var(--blue);color:var(--white);font-weight:600;font-size:18px;border-radius:6px;letter-spacing:.3px}
.dots{position:absolute;display:flex;gap:6px}
.dots span{width:14px;height:14px;border-radius:50%;border:2px solid var(--blue);background:var(--white)}
.dots span.on{background:var(--blue)}

/* header */
.site-header{position:absolute;left:0;top:0;width:1200px;height:89px;background:var(--white);z-index:3;border-bottom:1px solid #ddd}
.brand-badge{position:absolute;left:62px;top:2px;width:156px;height:156px;border-radius:50%;background:var(--white);box-shadow:0 4px 14px rgba(0,0,0,.18);z-index:4;display:flex;align-items:center;justify-content:center;text-align:center}
.brand-badge .name{font-weight:700;font-size:21px;line-height:1.15;color:var(--blue)}
.main-nav{position:absolute;left:338px;top:32px;display:flex;gap:0;font-size:19px;font-weight:500;color:var(--ink)}
.main-nav a{position:absolute;white-space:nowrap;color:inherit;text-decoration:none}
.header-phone{position:absolute;left:978px;top:28px;display:flex;gap:10px;align-items:center}
.header-phone small{display:block;font-size:10px;font-weight:500;color:var(--ink);line-height:1}
.header-phone strong{display:block;font-size:22px;font-weight:700;color:var(--accent);line-height:1.1}

/* hero */
.hero{position:absolute;left:0;top:0;width:1200px;height:720px;overflow:hidden}
.hero-photo{position:absolute;inset:0;background:linear-gradient(90deg,#ffffff 22%,#e7ecef 42%,#a9b9c6 62%,#5b7488 82%,#3f5668 100%)}
.hero-title{position:absolute;left:63px;top:222px;font-size:47px;font-weight:700;line-height:56px;color:var(--ink)}
.hero-title em{font-style:normal;color:var(--blue)}
.hero-text{position:absolute;left:65px;top:415px;font-size:16px;line-height:26px;color:var(--text)}

/* stats */
.stats{position:absolute;left:63px;top:651px;width:1074px;height:231px;background:var(--blue);border-radius:10px;display:grid;grid-template-columns:repeat(4,1fr);padding:0 80px}
.stat{text-align:center;color:var(--white);padding-top:40px}
.stat .ring{width:94px;height:94px;margin:0 auto 14px;border-radius:50%;background:var(--white);display:flex;align-items:center;justify-content:center}
.stat b{display:block;font-size:22px;font-weight:600;line-height:1.2}
.stat span{font-size:15px;font-weight:500}

/* about */
.about-title{position:absolute;left:64px;top:982px;font-size:42px;font-weight:600;color:var(--ink)}
.about-text{position:absolute;left:64px;width:480px;font-size:16px;line-height:28px}
.about-deco{position:absolute;left:665px;top:975px;width:510px;height:460px;background:#f1f1f1;border-radius:18px}
.photo-frame{position:absolute;border:6px solid var(--white);box-shadow:0 4px 18px rgba(0,0,0,.22);border-radius:8px}

/* services */
.services{position:absolute;left:0;top:1499px;width:1200px;height:542px;background:linear-gradient(100deg,var(--services-bg-a),var(--services-bg-b))}
.section-title{position:absolute;left:0;width:1200px;text-align:center;font-size:43px;font-weight:600;color:var(--ink)}
.section-lead{position:absolute;left:0;width:1200px;text-align:center;font-size:16px;line-height:28px;color:var(--text)}
.service-card{position:absolute;top:216px;width:258px;height:221px;background:var(--white);border-radius:6px;text-align:center;box-shadow:0 3px 10px rgba(0,0,0,.08)}
.service-card svg{margin-top:22px}
.service-card h3{position:absolute;left:0;right:0;top:150px;font-size:21px;font-weight:600;color:var(--ink)}
.service-card.active{background:var(--blue)}
.service-card.active h3{color:var(--white)}
.slider-arrow{position:absolute;width:42px;height:42px;border-radius:50%;background:var(--blue);border:3px solid var(--white);display:flex;align-items:center;justify-content:center}

/* savings */
.savings{position:absolute;left:0;top:2041px;width:1200px;height:517px;overflow:hidden}
.savings-photo{position:absolute;inset:0;background:linear-gradient(90deg,#7d7e82,#8f9094 50%,#9a9b9f)}
.savings-person{position:absolute;left:120px;top:65px;width:260px;height:452px;background:linear-gradient(180deg,#3c5aa8,#2e4a94);border-radius:120px 120px 0 0}
.savings-title{position:absolute;left:533px;top:107px;font-size:45px;font-weight:600;color:var(--white);letter-spacing:.5px}
.savings-text{position:absolute;left:537px;top:178px;width:480px;font-size:16px;line-height:28px;color:#f2f2f2}

/* blog */
.blog-card{position:absolute;top:2754px;width:350px;height:481px;background:var(--white);border-radius:8px;box-shadow:0 2px 10px rgba(0,0,0,.18);overflow:hidden}
.blog-card .thumb{height:233px}
.blog-card .date{position:absolute;right:0;top:212px;background:var(--white);color:var(--blue);font-size:15px;font-weight:500;padding:0 10px 0 14px;height:22px;line-height:22px;border-radius:8px 0 0 0}
.blog-card h3{position:absolute;left:16px;top:250px;font-size:19px;font-weight:600;line-height:25px;color:var(--ink)}
.blog-card p{position:absolute;left:16px;top:302px;width:320px;font-size:15px;line-height:22px;color:var(--text)}
.blog-card .btn{left:16px;top:401px;width:245px;height:51px}
.blog-card.featured{background:var(--blue)}
.blog-card.featured h3,.blog-card.featured p{color:var(--white)}
.blog-card.featured .btn{background:var(--white);color:var(--ink)}

/* contact */
.contact{position:absolute;left:0;top:3329px;width:1200px;height:500px;overflow:hidden}
.contact-photo{position:absolute;inset:0;background:linear-gradient(90deg,#2e4f66 0%,#41617a 35%,#4a4f55 60%,#3a3530 100%)}
.contact-person{position:absolute;left:110px;top:30px;width:250px;height:470px;background:linear-gradient(180deg,#3556a6,#29458c);border-radius:120px 120px 0 0}
.contact-title{position:absolute;left:596px;top:36px;font-size:44px;font-weight:600;color:var(--white)}
.field{position:absolute;background:var(--white);border-radius:6px;font-size:15px;color:var(--ink);padding:12px 18px}

/* footer */
.site-footer{position:absolute;left:0;top:3829px;width:1200px;height:355px;background:var(--footer);color:var(--white)}
.footer-brand{position:absolute;left:128px;top:70px;display:flex;align-items:center;gap:10px;font-size:22px;font-weight:700}
.footer-brand i{width:22px;height:22px;border-radius:50%;background:var(--white);display:block}
.footer-about{position:absolute;left:64px;top:178px;width:320px;font-size:15px;line-height:20px}
.footer-heading{position:absolute;font-size:18px;font-weight:600;color:var(--accent)}
.footer-list{position:absolute;list-style:none;font-size:15px}
.footer-list li{height:36px;display:flex;align-items:center;gap:14px}
.social-dot{width:22px;height:22px;border-radius:50%;background:var(--white);display:block}
.footer-rule{position:absolute;left:0;top:300px;width:1200px;height:1px;background:var(--footer-line)}
.footer-legal{position:absolute;top:318px;font-size:15px}
</style>
</head>
<body>

<!-- hero -->
<section class="hero">
  <div class="hero-photo" role="img" aria-label="Smiling plumber in a plaid shirt and tool belt working under a sink"></div>
  <h1 class="hero-title">Expert Plumbing<br>Services for <em>Every</em><br><em>Home!</em></h1>
  <p class="hero-text">Lorem ipsum odor amet, consectetuer adipiscing elit.<br>Hendrerit consequat</p>
  <a class="btn" style="left:63px;top:500px;width:246px;height:52px">CONTACT US</a>
  <div class="dots" style="left:572px;top:610px"><span class="on"></span><span></span><span></span></div>
</section>

<!-- header -->
<header class="site-header">
  <nav class="main-nav">
    <a style="left:0">HOME</a>
    <a style="left:92px">ABOUT US</a>
    <a style="left:222px">SERVICES</a>
    <a style="left:347px">BLOG</a>
    <a style="left:433px">CONTACT</a>
  </nav>
  <div class="header-phone">
    <svg width="30" height="30" viewBox="0 0 24 24" fill="none" stroke="#1b1b1b" stroke-width="1.5"><path d="M5 3h4l2 5-2.5 1.5a11 11 0 0 0 6 6L16 13l5 2v4a2 2 0 0 1-2 2A16 16 0 0 1 3 5a2 2 0 0 1 2-2z"/></svg>
    <div><small>Open 24 hours</small><strong>555 014 2298</strong></div>
  </div>
</header>
<div class="brand-badge"><span class="name">KT<br>Plumbline</span></div>

<!-- stats -->
<section class="stats">
  <div class="stat"><div class="ring"><svg width="52" height="52" viewBox="0 0 52 52" fill="none" stroke="#0b6e99" stroke-width="2"><rect x="4" y="6" width="14" height="10" rx="2"/><rect x="34" y="6" width="14" height="10" rx="2"/><rect x="19" y="36" width="14" height="10" rx="2"/><path d="M11 16v8h30v-8M26 24v12"/></svg></div><b>35</b><span>No of Branches</span></div>
  <div class="stat"><div class="ring"><svg width="52" height="52" viewBox="0 0 52 52" fill="none" stroke="#0b6e99" stroke-width="2"><rect x="10" y="6" width="26" height="38" rx="2"/><path d="M16 16h14M16 23h14M16 30h8"/><circle cx="36" cy="36" r="9"/><path d="M32 36l3 3 5-6"/></svg></div><b>1500</b><span>Projects completed</span></div>
  <div class="stat"><div class="ring"><svg width="52" height="52" viewBox="0 0 52 52" fill="none" stroke="#0b6e99" stroke-width="2"><path d="M14 44V30a12 12 0 0 1 24 0v14"/><path d="M16 18a10 10 0 0 1 20 0z"/><path d="M40 8l4 4-6 6-4-4zM38 18l-6 20"/></svg></div><b>25+</b><span>years of Experices</span></div>
  <div class="stat"><div class="ring"><svg width="52" height="52" viewBox="0 0 52 52" fill="none" stroke="#0b6e99" stroke-width="2"><circle cx="26" cy="26" r="20"/><circle cx="26" cy="26" r="14" stroke-dasharray="3 3"/><path d="M19 26l5 5 9-10"/></svg></div><b>1200</b><span>On Time Actions</span></div>
</section>

<!-- about -->
<section class="about">
  <h2 class="about-title">ABOUT US</h2>
  <p class="about-text" style="top:1051px">Lorem ipsum odor amet, consectetuer adipiscing elit. Mollis bibendum sagittis placerat donec eget finibus phasellus molestie. Laoreet accumsan litora ullamcorper lorem varius velit tincidunt. Magnis dignissim malesuada maximus vulputate donec. Hac mus nisi magnis congue id.</p>
  <p class="about-text" style="top:1214px">Lorem ipsum odor amet, consectetuer adipiscing elit. Mollis bibendum sagittis placerat donec eget finibus phasellus molestie. Laoreet accumsan</p>
  <a class="btn" style="left:63px;top:1327px;width:247px;height:52px">READ MORE</a>
  <div class="about-deco" role="img" aria-label="Faint pipe outline decoration"></div>
  <div class="photo-frame" style="left:805px;top:953px;width:312px;height:352px;background:linear-gradient(160deg,#9fb2c0,#5e7282 60%,#3f4d58)" role="img" aria-label="Plumber in grey overalls with arms crossed"></div>
  <div class="photo-frame" style="left:586px;top:1115px;width:306px;height:305px;background:linear-gradient(160deg,#d9d4cc,#8d8a86 55%,#3d3d3d)" role="img" aria-label="Plumber kneeling to repair pipes under a kitchen sink"></div>
</section>

<!-- services -->
<section class="services">
  <h2 class="section-title" style="top:46px">OUR SERVICES</h2>
  <p class="section-lead" style="top:116px">Lorem ipsum odor amet, consectetuer adipiscing elit. Mollis bibendum<br>sagittis placerat donec eget</p>
  <div class="service-card active" style="left:63px">
    <svg width="92" height="100" viewBox="0 0 92 100" fill="none" stroke="#fff" stroke-width="3"><path d="M10 70V44a10 10 0 0 1 10-10h40V12h10v34H30a6 6 0 0 0-6 6v18"/><path d="M6 70h22"/><path d="M50 60c-6 8-8 12-8 16a8 8 0 0 0 16 0c0-4-2-8-8-16z"/></svg>
    <h3>BLOCKED DEAINS</h3>
  </div>
  <div class="service-card" style="left:335px">
    <svg width="92" height="100" viewBox="0 0 92 100" fill="none" stroke="#0b6e99" stroke-width="3"><circle cx="46" cy="26" r="18"/><path d="M46 26l8-8"/><path d="M46 44v12M8 56h76v22H8zM30 56v22M62 56v22"/></svg>
    <h3>GAS&nbsp; FITTING</h3>
  </div>
  <div class="service-card" style="left:606px">
    <svg width="92" height="100" viewBox="0 0 92 100" fill="none" stroke="#0b6e99" stroke-width="3"><path d="M10 12h20v40h30V12h12v70H60M6 82h80"/><path d="M20 12v-4h20v4M30 52v16h20"/></svg>
    <h3>PLUMBING</h3>
  </div>
  <div class="service-card" style="left:879px">
    <svg width="92" height="100" viewBox="0 0 92 100" fill="none" stroke="#0b6e99" stroke-width="3"><rect x="18" y="8" width="56" height="74" rx="8"/><path d="M18 22h56M34 90v-8M46 90v-8M58 90v-8"/><circle cx="46" cy="52" r="14"/><path d="M48 42l-6 11h8l-6 10"/></svg>
    <h3>HOT WATER</h3>
  </div>
  <div class="slider-arrow" style="left:41px;top:306px"><svg width="16" height="16" viewBox="0 0 16 16" fill="none" stroke="#fff" stroke-width="2.5"><path d="M10 3L5 8l5 5"/></svg></div>
  <div class="slider-arrow" style="left:1114px;top:306px"><svg width="16" height="16" viewBox="0 0 16 16" fill="none" stroke="#fff" stroke-width="2.5"><path d="M6 3l5 5-5 5"/></svg></div>
  <div class="dots" style="left:572px;top:475px"><span class="on"></span><span></span><span></span></div>
</section>

<!-- savings -->
<section class="savings">
  <div class="savings-photo" role="img" aria-label="Plumbing tools scattered on a grey surface"></div>
  <svg class="abs" style="left:0;top:0" width="1200" height="517" viewBox="0 0 1200 517">
    <polygon points="0,0 210,0 0,175" fill="#fff"/>
    <polygon points="0,0 170,0 0,142" fill="#0b6e99"/>
    <polygon points="1200,517 945,517 1200,300" fill="#fff"/>
    <polygon points="1200,517 990,517 1200,338" fill="#0b6e99"/>
  </svg>
  <div class="savings-person" role="img" aria-label="Bearded plumber in blue overalls holding a piggy bank"></div>
  <h2 class="savings-title">SAVE YOUR MONEY</h2>
  <p class="savings-text">Lorem ipsum odor amet, consectetuer adipiscing elit. Mollis bibendum sagittis placerat donec eget finibus phasellus molestie. Laoreet accumsan litora ullamcorper lorem varius velit tincidunt. Magnis dignissim malesuada maximus vulputate donec. Hac mus nisi magnis congue id.</p>
  <a class="btn" style="left:537px;top:358px;width:290px;height:52px">VIEW SAVING&nbsp; PLAN <svg width="24" height="16" viewBox="0 0 24 16" fill="none" stroke="#fff" stroke-width="2"><path d="M1 8h21M15 2l7 6-7 6"/></svg></a>
</section>

<!-- blog -->
<section class="blog">
  <h2 class="section-title" style="top:2600px">BLOG</h2>
  <p class="section-lead" style="top:2670px;line-height:20px">Lorem ipsum odor amet, consectetuer adipiscing elit. Mollis bibendum sagittis<br>placerat donec eget finibus phasellus molestie.</p>
  <article class="blog-card" style="left:63px">
    <div class="thumb" role="img" aria-label="Plumbers repairing a wall-mounted sump pump" style="background:linear-gradient(135deg,#c9c3bb,#8a8580 60%,#b8c34a)"></div>
    <span class="date">April 6, 2024</span>
    <h3>sump pump<br>maintenance</h3>
    <p>Lorem ipsum odor amet, consectetuer adipiscing elit. Mollis bibendum sagittis placerat donec</p>
    <a class="btn">READ MORE</a>
  </article>
  <article class="blog-card featured" style="left:424px">
    <div class="thumb" role="img" aria-label="Plumber using a plunger on a white toilet" style="background:linear-gradient(135deg,#e9ecef,#b7c0c7 55%,#2e4c8a)"></div>
    <span class="date">Oct 10, 2024</span>
    <h3>Get a New<br>Comfortable Toilet</h3>
    <p>Lorem ipsum odor amet, consectetuer adipiscing elit. Mollis bibendum sagittis placerat donec</p>
    <a class="btn">READ MORE</a>
  </article>
  <article class="blog-card" style="left:786px">
    <div class="thumb" role="img" aria-label="Technician adjusting a manifold of colored pipes" style="background:linear-gradient(135deg,#6f8a5a,#9a7b5e 50%,#3c5c8a)"></div>
    <span class="date">May 25, 2023</span>
    <h3>Pluming<br>Tips</h3>
    <p>Lorem ipsum odor amet, consectetuer adipiscing elit. Mollis bibendum sagittis placerat donec</p>
    <a class="btn">READ MORE</a>
  </article>
  <div class="dots" style="left:572px;top:3272px"><span class="on"></span><span></span><span></span></div>
</section>

<!-- contact -->
<section class="contact">
  <div class="contact-photo" role="img" aria-label="Close-up of a plumber fitting a pipe under a sink"></div>
  <div class="contact-person" role="img" aria-label="Plumber in blue overalls giving a thumbs up"></div>
  <h2 class="contact-title">GET IN TOUCH</h2>
  <div class="field" style="left:596px;top:101px;width:263px;height:45px">Name</div>
  <div class="field" style="left:874px;top:101px;width:263px;height:45px">Services</div>
  <div class="field" style="left:596px;top:161px;width:541px;height:44px">Email Address</div>
  <div class="field" style="left:596px;top:219px;width:541px;height:44px">Phone</div>
  <div class="field" style="left:596px;top:278px;width:541px;height:96px;padding-top:8px">Leave message</div>
  <a class="btn" style="left:596px;top:406px;width:192px;height:52px">SUBMIT</a>
</section>

<!-- footer -->
<footer class="site-footer">
  <div class="footer-brand"><i></i>KT Plumbline</div>
  <p class="footer-about">Lorem ipsum odor amet, consectetuer adipiscing elit. Mollis bibendum sagittis placerat donec eget</p>

  <h4 class="footer-heading" style="left:476px;top:60px">Quick Link</h4>
  <ul class="footer-list" style="left:476px;top:101px">
    <li>Home</li><li>About Us</li><li>Services</li><li>Blog</li><li>Contact</li>
  </ul>

  <h4 class="footer-heading" style="left:689px;top:60px">FOLLOW US</h4>
  <ul class="footer-list" style="left:689px;top:101px;line-height:1">
    <li><i class="social-dot"></i>Friendbook</li>
    <li><i class="social-dot"></i>ViewTube</li>
    <li style="margin-top:4px"><i class="social-dot"></i>Chirper</li>
    <li><i class="social-dot"></i>Wiregram</li>
  </ul>

  <h4 class="footer-heading" style="left:919px;top:60px">OPEN HOURS</h4>
  <ul class="footer-list" style="left:919px;top:101px">
    <li><svg width="24" height="24" viewBox="0 0 24 24" fill="none" stroke="#fff" stroke-width="1.6"><circle cx="12" cy="12" r="10"/><path d="M12 6v6l4 2"/></svg>MON-SUN 24/7 HOURS</li>
  </ul>
  <h4 class="footer-heading" style="left:919px;top:155px">EMAIL</h4>
  <ul class="footer-list" style="left:919px;top:195px">
    <li><svg width="26" height="20" viewBox="0 0 26 20" fill="none" stroke="#fff" stroke-width="1.6"><rect x="1" y="1" width="24" height="18" rx="2"/><path d="M1 2l12 9 12-9"/></svg>hello@ktplumbline.example</li>
  </ul>

  <div class="footer-rule"></div>
  <p class="footer-legal" style="left:64px">© 2024 All Rights Reserved</p>
  <p class="footer-legal" style="right:64px">Privacy Policy | Team &amp; condition</p>
</footer>

</body>
</html>
```